Design packaging for a line of cell phone accessories

Hello,
we are seeking to develop the footprint for a line of cellphone accessories and gadgets. It will regard packaging for amongst others :
-bluetooth headphones
-powercases
-chargers
-Shopping bags
-cases
-cable
-etc
The entire line should carry the same design, but will obviously involve different product/sizes/specs. It's about the most original FOOTPRINT!!
The logo is attached
The design should contain the main colors: Orange on Black
I also added a die-cut and image of a product (solar charger) which should be redesigned per the above specifics

Cell Phone

• Gold on black

```html
<!DOCTYPE html>
<html lang="en">
<head>
<meta charset="utf-8">
<title>Solar Charger Packaging – Spine and Front Panel</title>
<link href="https://fonts.googleapis.com/css2?family=Quicksand:wght@500;600;700&display=swap" rel="stylesheet">
<style>
  :root {
    --canvas-bg: #ffffff;
    --box-black: #0a0a0a;
    --band-grey-light: #5c5c5c;
    --band-grey-dark: #1c1c1c;
    --accent-orange: #d9531e;
    --swoosh-white: #f2f2f2;
    --text-white: #f5f5f5;
    --product-light: #4a4a4a;
    --product-dark: #151515;
  }
  html, body {
    margin: 0;
    padding: 0;
    width: 1200px;
    height: 1200px;
    overflow: hidden;
    background: var(--canvas-bg);
  }
  .canvas {
    position: relative;
    width: 1200px;
    height: 1200px;
    font-family: "Quicksand", sans-serif;
  }
  .panel-artwork {
    position: absolute;
    inset: 0;
  }

  /* Spine */
  .spine-panel {
    position: absolute;
    left: 140px;
    top: 100px;
    width: 220px;
    height: 1000px;
    background: var(--box-black);
    overflow: hidden;
  }
  .spine-content {
    position: absolute;
    left: -390px;
    top: 390px;
    width: 1000px;
    height: 220px;
    transform: rotate(90deg);
  }
  .spine-title {
    position: absolute;
    left: 130px;
    top: 22px;
    margin: 0;
    font-weight: 600;
    line-height: 1;
  }
  .spine-title-row {
    display: flex;
    align-items: center;
    gap: 22px;
  }
  .spine-title-line-1 {
    font-size: 56px;
    color: var(--text-white);
  }
  .spine-tab {
    padding: 6px 14px;
    background: var(--accent-orange);
    font-size: 26px;
    font-weight: 700;
    color: var(--box-black);
  }
  .spine-title-line-2 {
    display: block;
    font-size: 96px;
    color: var(--accent-orange);
    margin-top: 2px;
  }
  .spine-brand {
    position: absolute;
    left: 770px;
    top: 70px;
    display: flex;
    align-items: center;
    gap: 10px;
  }
  .spine-brand .brand-dot {
    width: 34px;
    height: 34px;
  }
  .spine-brand .brand-name {
    font-size: 26px;
  }
  .spine-brand .brand-tagline {
    font-size: 12px;
    margin-top: 2px;
  }

  /* Front */
  .front-panel {
    position: absolute;
    left: 360px;
    top: 100px;
    width: 700px;
    height: 1000px;
    background: var(--box-black);
    overflow: hidden;
  }
  .brand {
    display: flex;
    align-items: center;
    gap: 16px;
  }
  .front-brand {
    position: absolute;
    top: 100px;
    left: 0;
    right: 0;
    justify-content: center;
  }
  .brand-dot {
    width: 58px;
    height: 58px;
    border-radius: 50%;
    background: var(--accent-orange);
  }
  .brand-text {
    display: flex;
    flex-direction: column;
  }
  .brand-name {
    font-size: 46px;
    font-weight: 700;
    color: var(--accent-orange);
    letter-spacing: 2px;
    line-height: 1;
  }
  .brand-tagline {
    font-size: 18px;
    font-weight: 600;
    color: var(--text-white);
    margin-top: 4px;
  }
  .product-photo {
    position: absolute;
    left: 175px;
    top: 270px;
    width: 350px;
    height: 420px;
    border-radius: 36px;
    background: linear-gradient(160deg, var(--product-light), var(--product-dark) 70%);
  }
  .product-title {
    position: absolute;
    left: 110px;
    top: 715px;
    margin: 0;
    font-weight: 600;
    line-height: 0.95;
  }
  .title-line-1 {
    display: block;
    font-size: 96px;
    color: var(--text-white);
  }
  .title-line-2 {
    display: block;
    font-size: 96px;
    color: var(--accent-orange);
    padding-left: 70px;
  }
  .feature-tab {
    position: absolute;
    right: 26px;
    bottom: 28px;
    padding: 8px 22px 8px 38px;
    background: var(--accent-orange);
    clip-path: polygon(16px 0, 100% 0, 100% 100%, 0 100%);
    font-size: 30px;
    font-weight: 700;
    color: var(--box-black);
  }
</style>
</head>
<body>
<div class="canvas">
  <aside class="spine-panel">
    <svg class="panel-artwork" width="220" height="1000" viewBox="0 0 220 1000" aria-hidden="true">
      <defs>
        <linearGradient id="spineBand" x1="0" y1="0" x2="0" y2="1">
          <stop offset="0" stop-color="var(--band-grey-dark)"/>
          <stop offset="1" stop-color="var(--band-grey-light)"/>
        </linearGradient>
      </defs>
      <path class="grey-band" d="M0 560 L220 500 L220 650 C140 640 70 650 0 665 Z" fill="url(#spineBand)"/>
      <path class="top-swoosh" d="M90 0 C140 40 180 80 220 110 L220 125 C170 90 130 50 75 0 Z" fill="var(--swoosh-white)"/>
      <path class="bottom-swoosh" d="M0 660 C70 645 140 638 220 645 L220 657 C140 650 70 658 0 673 Z" fill="var(--swoosh-white)"/>
    </svg>
    <div class="spine-content">
      <h2 class="spine-title">
        <span class="spine-title-row">
          <span class="spine-title-line-1">Solar</span>
          <span class="spine-tab">with USB hub</span>
        </span>
        <span class="spine-title-line-2">Charger</span>
      </h2>
      <div class="brand spine-brand">
        <span class="brand-dot"></span>
        <div class="brand-text">
          <span class="brand-name">VOLTRA</span>
          <span class="brand-tagline">Accessories and gadgets</span>
        </div>
      </div>
    </div>
  </aside>

  <section class="front-panel">
    <svg class="panel-artwork" width="700" height="1000" viewBox="0 0 700 1000" aria-hidden="true">
      <defs>
        <linearGradient id="bandGradient" x1="1" y1="0" x2="0" y2="1">
          <stop offset="0" stop-color="var(--band-grey-light)"/>
          <stop offset="1" stop-color="var(--band-grey-dark)"/>
        </linearGradient>
      </defs>
      <path class="grey-band" d="M700 200 C540 320 270 380 0 460 L0 780 C270 710 500 700 700 730 Z" fill="url(#bandGradient)"/>
      <path class="top-swoosh" d="M0 18 C180 160 430 295 700 295 L700 308 C420 312 170 180 0 36 Z" fill="var(--swoosh-white)"/>
      <path class="bottom-swoosh" d="M0 740 C250 688 500 692 700 722 L700 733 C500 705 260 705 0 754 Z" fill="var(--swoosh-white)"/>
      <rect class="inner-frame" x="25" y="26" width="650" height="948" fill="none" stroke="var(--accent-orange)" stroke-width="3"/>
    </svg>

    <div class="brand front-brand">
      <span class="brand-dot"></span>
      <div class="brand-text">
        <span class="brand-name">VOLTRA</span>
        <span class="brand-tagline">Accessories and gadgets</span>
      </div>
    </div>

    <div class="product-photo" role="img" aria-label="Product photo: black square solar charger with silver rim and dock connector"></div>

    <h1 class="product-title">
      <span class="title-line-1">Solar</span>
      <span class="title-line-2">Charger</span>
    </h1>

    <div class="feature-tab">with USB hub</div>
  </section>
</div>
</body>
</html>
```